Bramblewood Craft Spirits Bottle Label

Bramblewood Craft Spirits is a distillery and craft cocktail bar that will be located in Calgary, Alberta, Canada. Here, we create awesome hand crafted spirits like vodka, gin, rum, whiskey, brandy, liqueurs etc. We need bottle labels for 3 different initial products. The names of the products are as follows, Orchard Dash Gin (22% alc/vol), Toverin Dry Gin (40% alc/vol), and Palundro Contemporary Gin (40% alc/vol). It would be preferable to have 3 distinct labels. The alcohol by volume declaration must be on the front display of the label, without having to turn the bottle. There is a logo for Bramblewood Craft Spirits I would like featured in the front around 1''x1" or 2.5cm x 2.5cm in size. Some last minute changes are being made to the logo so it is not uploaded at this moment. Abstract geometry would be a great fit for the contemporary gin and I have attached an example.Simple or complex designs both encouraged. The Orchard Dash Gin will be in the Moonea style bottle and the other two will be in Apotheker style bottles. Thank you so much to anyone interested in participating and we can't wait to hear from you. This is a great opportunity to showcase your creativity and be involved with future products!
Young professionals ages 21-30.

```html
<!DOCTYPE html>
<html lang="en">
<head>
<meta charset="utf-8">
<title>Orchard Dash Gin – Label Variants</title>
<link href="https://fonts.googleapis.com/css2?family=Saira+Stencil+One&family=Saira+Semi+Condensed:wght@600;700;800&display=swap" rel="stylesheet">
<style>
  :root {
    --backdrop: #ffc999;
    --ink: #231f20;
    --paper-white: #ffffff;
    --paper-navy: #262262;
    --paper-cream: #efebd2;
    --accent-orange: #f7941d;
    --pattern-yellow: #ffd51f;
    --pattern-teal: #00b2a9;
    --pattern-orange: #f7941d;
    --pattern-charcoal: #414042;
    --pattern-red: #ef5a2f;
    --pattern-cream: #fdf3dc;
    --swatch-lilac: #9490b2;
    --swatch-sage: #c8e29e;
  }
  * { box-sizing: border-box; margin: 0; padding: 0; }
  html, body { width: 1200px; height: 1200px; overflow: hidden; }
  body {
    background: var(--backdrop);
    font-family: "Saira Semi Condensed", "Arial Narrow", sans-serif;
    position: relative;
  }
  .label-lineup {
    position: absolute;
    left: 89px;
    top: 181px;
    display: flex;
    gap: 46px;
  }
  .label {
    position: relative;
    width: 310px;
    height: 745px;
    background: var(--paper);
    color: var(--text);
    border: 2px solid var(--ink);
  }
  .label--white { --paper: var(--paper-white); --text: var(--ink); --swatch: var(--swatch-lilac); }
  .label--navy  { --paper: var(--paper-navy);  --text: #ffffff;    --swatch: var(--swatch-sage); border-color: var(--paper-navy); }
  .label--cream { --paper: var(--paper-cream); --text: var(--ink); --swatch: var(--swatch-lilac); border-color: var(--paper-cream); }
  .label--navy::before {
    content: "";
    position: absolute;
    inset: 6px;
    border: 2px solid #ffffff;
    pointer-events: none;
  }
  .origin-line {
    position: absolute;
    top: 34px;
    left: 30px;
    right: 30px;
    display: flex;
    justify-content: space-between;
    font-size: 9px;
    font-weight: 800;
    letter-spacing: 0.3px;
  }
  .product-name {
    position: absolute;
    top: 52px;
    left: 0;
    right: 0;
    text-align: center;
    font-family: "Saira Stencil One", "Impact", sans-serif;
    font-size: 25px;
    line-height: 1;
    letter-spacing: 0.5px;
  }
  .name-rule {
    position: absolute;
    top: 86px;
    left: 32px;
    right: 32px;
    height: 7px;
    background: var(--text);
  }
  .maker-mark {
    position: absolute;
    top: 100px;
    left: 0;
    right: 0;
    display: flex;
    flex-direction: column;
    align-items: center;
    gap: 6px;
  }
  .maker-mark__row {
    display: flex;
    align-items: center;
    gap: 14px;
  }
  .maker-mark__rule {
    width: 52px;
    height: 2px;
    background: var(--text);
  }
  .maker-mark__dot {
    width: 34px;
    height: 34px;
    border-radius: 50%;
    background: var(--accent-orange);
  }
  .maker-mark__name {
    font-size: 12px;
    font-weight: 800;
    letter-spacing: 1px;
    text-transform: uppercase;
  }
  .pattern-panel {
    position: absolute;
    left: 19px;
    top: 182px;
    width: 272px;
    height: 500px;
    border: 2px solid var(--ink);
    overflow: hidden;
  }
  .pattern-panel__art {
    position: absolute;
    inset: 0;
    background:
      linear-gradient(135deg, var(--pattern-yellow) 0%, var(--pattern-cream) 18%, var(--pattern-charcoal) 30%, var(--pattern-teal) 46%, var(--pattern-yellow) 60%, var(--pattern-teal) 72%, var(--pattern-orange) 88%, var(--pattern-orange) 100%);
  }
  .flavour-window {
    position: absolute;
    left: 40px;
    top: 326px;
    width: 197px;
    height: 174px;
    background: #ffffff;
    border: 1px solid var(--pattern-yellow);
  }
  .flavour-window__swatch {
    position: absolute;
    left: 19px;
    top: 19px;
    right: 19px;
    bottom: 0;
    background: var(--swatch);
  }
  .volume-line {
    position: absolute;
    top: 700px;
    left: 19px;
    right: 19px;
    display: flex;
    align-items: center;
    gap: 10px;
    font-size: 17px;
    font-weight: 700;
  }
  .volume-line__rule {
    flex: 1;
    height: 3px;
    background: var(--text);
  }
</style>
</head>
<body>
  <main class="label-lineup">
    <article class="label label--white">
      <div class="origin-line"><span>CALGARY</span><span>CANADA</span></div>
      <h1 class="product-name">ORCHARD DASH GIN</h1>
      <div class="name-rule"></div>
      <div class="maker-mark">
        <div class="maker-mark__row"><span class="maker-mark__rule"></span><span class="maker-mark__dot"></span><span class="maker-mark__rule"></span></div>
        <span class="maker-mark__name">Bramblewood Craft Spirits</span>
      </div>
      <div class="pattern-panel">
        <div class="pattern-panel__art" role="img" aria-label="Abstract geometric pattern of wavy stripes, quarter circles and rings in yellow, teal, orange and charcoal"></div>
        <div class="flavour-window"><div class="flavour-window__swatch"></div></div>
      </div>
      <div class="volume-line"><span>750ml</span><span class="volume-line__rule"></span><span>22% alc</span></div>
    </article>

    <article class="label label--navy">
      <div class="origin-line"><span>CALGARY</span><span>CANADA</span></div>
      <h1 class="product-name">ORCHARD DASH GIN</h1>
      <div class="name-rule"></div>
      <div class="maker-mark">
        <div class="maker-mark__row"><span class="maker-mark__rule"></span><span class="maker-mark__dot"></span><span class="maker-mark__rule"></span></div>
        <span class="maker-mark__name">Bramblewood Craft Spirits</span>
      </div>
      <div class="pattern-panel">
        <div class="pattern-panel__art" role="img" aria-label="Abstract geometric pattern of wavy stripes, quarter circles and rings in yellow, teal, orange and charcoal"></div>
        <div class="flavour-window"><div class="flavour-window__swatch"></div></div>
      </div>
      <div class="volume-line"><span>750ml</span><span class="volume-line__rule"></span><span>22% alc</span></div>
    </article>

    <article class="label label--cream">
      <div class="origin-line"><span>CALGARY</span><span>CANADA</span></div>
      <h1 class="product-name">ORCHARD DASH GIN</h1>
      <div class="name-rule"></div>
      <div class="maker-mark">
        <div class="maker-mark__row"><span class="maker-mark__rule"></span><span class="maker-mark__dot"></span><span class="maker-mark__rule"></span></div>
        <span class="maker-mark__name">Bramblewood Craft Spirits</span>
      </div>
      <div class="pattern-panel">
        <div class="pattern-panel__art" role="img" aria-label="Abstract geometric pattern of wavy stripes, quarter circles and rings in yellow, teal, orange and charcoal"></div>
        <div class="flavour-window"><div class="flavour-window__swatch"></div></div>
      </div>
      <div class="volume-line"><span>750ml</span><span class="volume-line__rule"></span><span>22% alc</span></div>
    </article>
  </main>
</body>
</html>
```